Marrowgate Auctions Business Cards Design Needed

I need a business card design that is modern looking - double sided (maybe just my logo on the back, but open to suggestions) - the overall design is up to you. I want it to be easy to read - not over the top flashy. I already have a company logo which I uploaded so that needs to be used. The colors of my logo are the colors I want on the card... so blue and gray (do need to match the logo colors).

Requirements
Must have
• Would like the card to be sleek, modern and easy to ready

```html
<!DOCTYPE html>
<html lang="en">
<head>
<meta charset="utf-8">
<title>Marrowgate Auctions Business Cards</title>
<link href="https://fonts.googleapis.com/css2?family=Open+Sans:wght@400;600;700&display=swap" rel="stylesheet">
<style>
  :root {
    --brand-blue: #2b74b8;
    --brand-blue-light: #3c8ac6;
    --text-gray: #55565b;
    --paper: #ffffff;
    --backdrop: #e7e9ec;
  }
  * { box-sizing: border-box; margin: 0; padding: 0; }
  html, body {
    width: 1200px; height: 892px; overflow: hidden;
    background: var(--backdrop);
    font-family: "Open Sans", Arial, sans-serif;
  }
  .stage { position: relative; width: 1200px; height: 892px; }
  .card {
    position: absolute; width: 520px; height: 298px;
    box-shadow: 0 8px 24px rgba(0,0,0,0.18);
    overflow: hidden;
  }
  .card-front {
    left: 70px; top: 130px;
    background: linear-gradient(160deg, var(--brand-blue-light), var(--brand-blue));
    color: var(--paper);
    display: flex; flex-direction: column; align-items: center; justify-content: center;
  }
  .front-wordmark {
    font-weight: 700; font-size: 46px; letter-spacing: 0.5px;
    display: flex; align-items: center; gap: 12px;
    margin-top: -10px;
  }
  .front-wordmark .mark-square { width: 22px; height: 22px; background: var(--paper); }
  .front-tagline {
    position: absolute; bottom: 46px; width: 100%; text-align: center;
    font-size: 14px; font-weight: 400;
  }
  .card-back { left: 610px; top: 460px; background: var(--paper); }
  .back-wordmark {
    position: absolute; left: 34px; top: 62px;
    display: flex; align-items: center; gap: 10px;
    color: var(--brand-blue); font-weight: 700; font-size: 27px; line-height: 1.05;
  }
  .back-wordmark .mark-square { width: 16px; height: 16px; background: var(--brand-blue); flex: none; }
  .contact {
    position: absolute; right: 34px; top: 98px; text-align: right;
  }
  .contact-name { color: var(--brand-blue); font-weight: 700; font-size: 19px; letter-spacing: 0.3px; }
  .contact-title { color: var(--text-gray); font-size: 13px; margin-top: 1px; }
  .contact-rule { height: 2px; background: var(--brand-blue); margin: 8px 0 8px auto; width: 140px; }
  .contact-line {
    color: var(--text-gray); font-size: 13px;
    display: flex; justify-content: flex-end; align-items: center; gap: 8px; margin-top: 3px;
  }
  .contact-line svg { width: 13px; height: 13px; fill: var(--brand-blue); }
  .footer-band {
    position: absolute; left: 0; bottom: 0; width: 520px; height: 36px;
    background: var(--brand-blue);
  }
  .footer-url {
    position: absolute; right: 34px; bottom: 9px;
    color: var(--paper); font-size: 15px; letter-spacing: 0.6px;
  }
</style>
</head>
<body>
<main class="stage">
  <section class="card card-front" aria-label="Card front">
    <div class="front-wordmark"><span class="mark-square"></span>Marrowgate</div>
    <p class="front-tagline">Improving Charity Auctions Nationwide</p>
  </section>

  <section class="card card-back" aria-label="Card back">
    <div class="back-wordmark"><span class="mark-square"></span><span>Marrowgate<br>Auctions</span></div>

    <div class="contact">
      <p class="contact-name">COLIN MARSH</p>
      <p class="contact-title">Owner/President - Auctioneer</p>
      <div class="contact-rule"></div>
      <p class="contact-line">702-555-0148
        <svg viewBox="0 0 16 16" aria-hidden="true"><path d="M3 2h3l1.5 3.5-2 1.2a8 8 0 0 0 3.8 3.8l1.2-2L14 10v3a1 1 0 0 1-1 1A12 12 0 0 1 2 3a1 1 0 0 1 1-1z"/></svg>
      </p>
      <p class="contact-line">marrowgatebids@mail.com
        <svg viewBox="0 0 16 16" aria-hidden="true"><path d="M1 3h14v10H1z M1 3l7 6 7-6" stroke="#fff" stroke-width="1"/></svg>
      </p>
    </div>

    <div class="footer-band"></div>
    <p class="footer-url">www.bidrescuegroup.com</p>
  </section>
</main>
</body>
</html>
```